CRPG is needing business cards, and stationary created.

Pixel Forge created a logo for our business, and now we are wanting business cards, and stationary. I have included two designs of the same logo. Please feel free to use them as you want. The name of the company is Cedar Ridge Property Group LLC, the address is 812 NE Willow Ln., Suite 9, the city & state is Bend, Oregon, zip code is 97815, Telephone number is 541-327-4489, Fax number is 541-327-6051, the name on the business card is Carl Whitby CMCA

Industry/Entity Type

Property Management

Contact Information for Business Card

The card needs to look professional. Upscale.

Requirements
Must have
• The colors we are using are on the logo that has been uploaded.

```html
<!DOCTYPE html>
<html lang="en">
<head>
<meta charset="utf-8">
<title>Cedar Ridge Property Group – Business Card</title>
<link rel="stylesheet" href="https://fonts.googleapis.com/css2?family=Montserrat:wght@600;700&family=Questrial&display=swap">
<style>
  :root{
    --stage:#3b3c3f;
    --slate:#3d4a5c;
    --teal:#1b8c7b;
    --ink:#3a4556;
    --muted:#555c66;
    --paper:#ffffff;
  }
  *{box-sizing:border-box;margin:0;padding:0}
  html,body{width:1200px;height:960px;overflow:hidden;background:var(--stage)}
  .canvas{position:relative;width:1200px;height:960px}
  .card{position:absolute;width:600px;height:343px;border-radius:26px;overflow:hidden}
  .card--front{left:110px;top:100px;background:var(--slate)}
  .card--back{left:490px;top:510px;background:var(--paper)}

  .brand{display:flex;align-items:center;gap:16px}
  .brand__mark{width:34px;height:34px;flex:none}
  .brand__name{font-family:"Montserrat",sans-serif;font-weight:700;line-height:1.05;letter-spacing:.02em}
  .brand__name .big{display:block;font-size:40px}
  .brand__name .small{display:block;font-size:15px;letter-spacing:.32em;margin-top:6px}
  .brand__rule{height:1.5px;margin-top:12px}

  .card--front .brand-wrap{position:absolute;left:50%;top:50%;transform:translate(-50%,-50%);text-align:left}
  .card--front .brand__mark{background:var(--paper)}
  .card--front .brand__name{color:var(--paper)}
  .card--front .brand__rule{background:var(--paper)}

  .card--back .brand-wrap{position:absolute;left:38px;top:128px;width:215px}
  .card--back .brand{gap:10px;align-items:flex-start}
  .card--back .brand__mark{width:24px;height:24px;background:var(--ink);margin-top:4px}
  .card--back .brand__name{color:var(--teal)}
  .card--back .brand__name .big{font-size:27px}
  .card--back .brand__name .small{font-size:10.5px;letter-spacing:.24em;margin-top:5px}
  .card--back .brand__rule{background:var(--ink)}

  .divider{position:absolute;left:272px;top:62px;width:1.5px;height:205px;background:var(--ink)}

  .contact{position:absolute;left:300px;top:68px;font-family:"Questrial",sans-serif;color:var(--muted)}
  .contact__name{font-family:"Montserrat",sans-serif;font-weight:700;font-size:28px;color:var(--teal);letter-spacing:.02em;line-height:1}
  .contact__title{font-size:17px;color:var(--muted);margin:6px 0 18px;letter-spacing:.02em}
  .contact__list{list-style:none}
  .contact__row{display:flex;align-items:flex-start;gap:12px;font-size:16px;line-height:1.25;margin-bottom:9px}
  .contact__row svg{width:16px;height:16px;flex:none;margin-top:2px;fill:var(--teal)}
  .contact__row--address{margin-top:12px}

  .band{position:absolute;left:0;right:0;bottom:0;height:22px;background:var(--teal)}
</style>
</head>
<body>
<main class="canvas">

  <section class="card card--front" aria-label="Card front">
    <div class="brand-wrap">
      <div class="brand">
        <span class="brand__mark" aria-hidden="true"></span>
        <p class="brand__name"><span class="big">CEDAR RIDGE</span><span class="small">PROPERTY GROUP</span></p>
      </div>
      <div class="brand__rule"></div>
    </div>
  </section>

  <section class="card card--back" aria-label="Card back">
    <div class="brand-wrap">
      <div class="brand">
        <span class="brand__mark" aria-hidden="true"></span>
        <p class="brand__name"><span class="big">CEDAR RIDGE</span><span class="small">PROPERTY GROUP</span></p>
      </div>
      <div class="brand__rule"></div>
    </div>

    <div class="divider"></div>

    <div class="contact">
      <h1 class="contact__name">YOUR NAME</h1>
      <p class="contact__title">YOUR TITLE</p>
      <ul class="contact__list">
        <li class="contact__row">
          <svg viewBox="0 0 24 24" aria-hidden="true"><path d="M6.6 10.8a15 15 0 0 0 6.6 6.6l2.2-2.2c.3-.3.7-.4 1-.2 1.1.4 2.3.6 3.6.6.6 0 1 .4 1 1V20c0 .6-.4 1-1 1A17 17 0 0 1 3 4c0-.6.4-1 1-1h3.5c.6 0 1 .4 1 1 0 1.3.2 2.5.6 3.6.1.3 0 .7-.2 1z"/></svg>
          <span>123-456-2100</span>
        </li>
        <li class="contact__row">
          <svg viewBox="0 0 24 24" aria-hidden="true"><path d="M2 5h20v14H2zm2 2v.4l8 5.2 8-5.2V7zm0 2.8V17h16V9.8l-8 5.2z"/></svg>
          <span>youremail@mailbox.com</span>
        </li>
        <li class="contact__row">
          <svg viewBox="0 0 24 24" aria-hidden="true"><path d="M12 2a10 10 0 1 0 0 20 10 10 0 0 0 0-20zm6.9 6h-3a15 15 0 0 0-1.3-3.9A8 8 0 0 1 18.9 8zM12 4c.8 1.2 1.5 2.5 1.9 4h-3.8c.4-1.5 1.1-2.8 1.9-4zM4.3 14a8 8 0 0 1 0-4h3.4a16 16 0 0 0 0 4zm.8 2h3a15 15 0 0 0 1.3 3.9A8 8 0 0 1 5.1 16zm3-8h-3a8 8 0 0 1 4.3-3.9C8.8 5.3 8.4 6.6 8.1 8zM12 20c-.8-1.2-1.5-2.5-1.9-4h3.8c-.4 1.5-1.1 2.8-1.9 4zm2.3-6H9.7a14 14 0 0 1 0-4h4.6a14 14 0 0 1 0 4zm.3 5.9c.6-1.2 1-2.5 1.3-3.9h3a8 8 0 0 1-4.3 3.9zm1.7-5.9a16 16 0 0 0 0-4h3.4a8 8 0 0 1 0 4z"/></svg>
          <span>www.yourwebsite.com</span>
        </li>
        <li class="contact__row contact__row--address">
          <svg viewBox="0 0 24 24" aria-hidden="true"><path d="M12 2a7 7 0 0 0-7 7c0 5.2 7 13 7 13s7-7.8 7-13a7 7 0 0 0-7-7zm0 9.5A2.5 2.5 0 1 1 12 6.5a2.5 2.5 0 0 1 0 5z"/></svg>
          <span>Your address, city<br>state, ZIP 0000</span>
        </li>
      </ul>
    </div>

    <div class="band"></div>
  </section>

</main>
</body>
</html>
```